Talbrin Business Cards

Front and back. Simon Kavelle MBA is the CEO of Talbrin Homes. Black white and grays. Logo and cool design.

Target Market(s)

Professional lenders and investors

Industry/Entity Type

Real estate developer. NO HOUSES OR ROOFS

Contact Information for Business Card

Logo, name and unique design. Front and back. Simon Kavelle MBA is the CEO of Talbrin Homes. Black white and grays. Logo and cool design.

Font styles to use
Sans Serif

Colors

Designer to choose only greyscale colors for use in the design.

Requirements
Must have
• Cool look. Not the same card I could design.
Nice to have
• Something memorable
Should not have
• Basic

```html
<!DOCTYPE html>
<html lang="en">
<head>
<meta charset="utf-8">
<title>Talbrin Homes – Business Cards</title>
<link href="https://fonts.googleapis.com/css2?family=Montserrat:wght@300;400;600;800&display=swap" rel="stylesheet">
<style>
  :root {
    --backdrop: #3a3a3c;
    --card-white: #f7f7f7;
    --card-black: #0c0c0c;
    --ink-dark: #111111;
    --ink-light: #f2f2f2;
    --rule: #8a8a8a;
  }
  * { margin: 0; padding: 0; box-sizing: border-box; }
  html, body {
    width: 1200px;
    height: 900px;
    overflow: hidden;
    background: var(--backdrop);
    font-family: "Montserrat", sans-serif;
  }
  .canvas {
    position: relative;
    width: 1200px;
    height: 900px;
  }
  .card {
    position: absolute;
    width: 560px;
    height: 320px;
    box-shadow: 0 14px 30px rgba(0, 0, 0, 0.45);
    display: flex;
    flex-direction: column;
    align-items: center;
    justify-content: center;
  }
  .card--front {
    left: 180px;
    top: 90px;
    background: var(--card-white);
  }
  .card--back {
    left: 460px;
    top: 480px;
    background: var(--card-black);
    color: var(--ink-light);
  }
  .wordmark {
    font-weight: 800;
    font-size: 58px;
    letter-spacing: -1.5px;
    line-height: 1;
    color: var(--ink-dark);
  }
  .card--back .wordmark {
    font-size: 44px;
    color: var(--ink-light);
  }
  .details {
    margin-top: 20px;
    width: 340px;
    text-align: center;
  }
  .rule {
    height: 1px;
    background: var(--rule);
  }
  .holder-name {
    font-weight: 600;
    font-size: 27px;
    letter-spacing: 1px;
    text-transform: uppercase;
    padding: 10px 0;
  }
  .holder-title {
    font-weight: 300;
    font-size: 24px;
    letter-spacing: 12px;
    padding-top: 10px;
    padding-left: 12px;
  }
</style>
</head>
<body>
  <main class="canvas">
    <section class="card card--front" aria-label="Card front">
      <div class="wordmark">Talbrin Homes</div>
    </section>

    <section class="card card--back" aria-label="Card back">
      <div class="wordmark">Talbrin Homes</div>
      <div class="details">
        <div class="rule"></div>
        <div class="holder-name">Simon Kavelle</div>
        <div class="rule"></div>
        <div class="holder-title">MBA | CEO</div>
      </div>
    </section>
  </main>
</body>
</html>
```